Bright Years Forward an age management group needs a modern looking website developed asap

Bright Years Forward is an age management group lead by a board certified medical doctor (who also specializes in age management medicine) and a 7th degree black belt jiu-jitsu master. Both have joined forces to create a unique doctor supervised anti-aging medical, nutritional, hormonal, exercise protocol never seen before.
This marriage between medicine and athleticism will create the worlds first complete anti-aging program designed for anyone wishing to remain as healthy and as young for as long as possible.

Our Mission and Vision: "To provide clients cutting edge anti aging programs and protocols designed to "turn-back-the-clock-one-second-at-a-time. Let's all Bright Years Forward..together!"

Bright Years Forward's program consists of 6 unique tiers/platforms each encompassing a specific need.
The 6 tiers are:
1. Apex Care: A medical doctor supervised unique and proprietary hormone optimization program and protocol developed by a board certified medical doctor trained by Volarix ( a world leader in age management medicine) who has practiced age management medicine for the past 7 years
2. Apex Slim: A medical doctor supervised unique and proprietary weight management program and protocol developed by a published medical doctor who's diet book "Fresh start: Shed those pounds soon" was just launched
3.Apex Motion: A master athlete supervised training program and protocol, with access to a large proprietary exercise video databank developed by a 7th degree black belt jiu-jitsu master.
4. Apex Plate: A chef driven and supervised home delivered healthy meals. Each meal is made from scratch, and is specifically tailored and targeted according to each patient's specific needs.
5. ApexDailyMix: A doctor formulated-master athlete approved most complete multi vitamin-mineral-anti-oxidant and supplement pack available on the market today. ApexDailyMix is: made in the USA, and QSA approved vitamin factory, gluten free, sugar free, and artificial color free.
6. Apex Academy: A unique CME approved teaching workshop intended for those physicians who lack expertise in age management but want to become proficient in the art of hormone optimization and age management medicine. The 2-day workshop is held twice monthly on Saturday and Sunday in sunny Florida.

This is our scope and goal.
We want to become the leaders in age management medicine by being the first to unite doctors-athletes-chefs-nutritionist together in an effort to deliver the most advanced most cutting edge programs and protocols so we may all : BRIGHT YAERS FORWARD!

We already have the logo for Bright years forward.
Please keep in mind the following:
1. Apex care should be in green and black
2. Apex slim should be in purple and black
3. Apex motion in orange and black
4. Apx plate in yellow and black
5. ApexDialyMix in red and black
6. Apex academy in gray and black

Target Market(s)

Adults Males and females wishing to remain as healthy and as young for as long as possible
Obese and overweight adults males and females
Athletes males and females
Young obese and overweight males and females
ALL can be from any country!

Industry/Entity Type

Health And Wellness

Coding

Coded - Design and coding required

Number of Pages Required

5+ page

Requirements
Must have
• The front page must have our mission statement as well as the 6 tiers/platforms displayed (Apex Care, Apex Slim, Apex Motion, Apex Plate, ApexDailyMix, Apex Academy) and each platform when "cliked on" should open up in its own unique page.
• The capability for clients to log on to any of the pages using assigned usernames and passwords.
• The capability of check out (credit cards, paypal) from any of the pages. EX the client may want to buy ApexDailyMix. He/She would click on the main page then click on ApexDailymix page and choose to buy the vitamin. Same For the rest: He/she may want to buy the weight loss program (apex slim), or the Hormone program (apex care) or the food delivered home (apex Plate) or apex motion (access to the exercise video databank) or attend the workshop (buy the teaching program..BUT this will ONLY be accessible if the client is a medical doctor and has a valid medical license).
• Also the client may want to have full access to ALL the 6 tiers, thus on the FRONT page we need a checkout with "full access to tiers"
• Also we need to make sure no videos are downloade but only viewed. we need to have this safety built in.
• Also we nee to be able to keep track of emails and have stats. and any email inquiry must be diverted to my iphone.
Nice to have
• Modern look with pop-ups and graphics and iphone and android capability
Should not have
• nothing explicit

```html
<!DOCTYPE html>
<html lang="en">
<head>
<meta charset="utf-8">
<title>Bright Years Forward</title>
<link href="https://fonts.googleapis.com/css2?family=Roboto:wght@400;500;700&family=Kaushan+Script&display=swap" rel="stylesheet">
<style>
:root{
  --topbar:#eef5fc;
  --ink:#1e1e1e;
  --muted:#555;
  --accent:#3d8ef0;
  --footer:#5da2f4;
  --footer-line:#3f7fd0;
  --card:#0c0c0c;
  --care:#0d8a0d;
  --slim:#7d0f86;
  --motion:#f6a10a;
  --plate:#c9cc0b;
  --mix:#ee0a0a;
  --academy:#777;
  --white:#fff;
}
*{margin:0;padding:0;box-sizing:border-box}
html,body{width:1200px;height:2406px;overflow:hidden;background:#fff}
body{position:relative;font-family:'Roboto',sans-serif;color:var(--ink)}
.abs{position:absolute}
.topbar{left:0;top:0;width:1200px;height:45px;background:var(--topbar);display:flex;align-items:center;justify-content:center}
.brand{font-weight:700;font-size:26px;color:#222;letter-spacing:.5px}
.hero{left:0;top:45px;width:1200px;height:547px;background:linear-gradient(180deg,#4d6a86 0%,#8aa0ae 30%,#a38552 62%,#4a3a22 100%)}
.nav{left:0;top:66px;width:1200px;height:28px}
.nav a{position:absolute;top:0;color:var(--white);font-size:15px;text-decoration:none;line-height:28px}
.login{background:var(--accent);border-radius:5px;padding:0 14px;height:33px;line-height:33px!important;top:-2px!important}
.hero-title{left:0;width:1200px;top:212px;padding-left:290px;text-align:center;font-family:'Kaushan Script',cursive;color:var(--white);font-size:74px;line-height:90px}
.hero-sub{left:0;width:1200px;top:312px;padding-left:275px;text-align:center;color:var(--white);font-weight:700;font-size:22px}
.btn{top:369px;height:34px;font-size:10px;font-weight:700;color:var(--white);display:flex;align-items:center;justify-content:center;text-transform:uppercase;border-radius:2px}
.btn-buy{left:624px;width:125px;background:var(--accent)}
.btn-surf{left:760px;width:106px;border:1.5px solid #e8e8e8}
.section-title{left:0;width:1200px;text-align:center;font-weight:700;font-size:22px;color:#222}
.rule{left:53px;width:1094px;border-top:1.5px dashed #8a8a8a}
.mission-label{left:53px;top:690px;width:247px;height:27px;background:var(--accent);color:var(--white);font-weight:700;font-size:17px;display:flex;align-items:center;justify-content:center;border-radius:2px}
.mission-text{left:310px;top:688px;width:760px;font-size:13px;line-height:19px;color:#555}
.devices{left:156px;top:770px;width:956px;height:457px;background:linear-gradient(180deg,#e9eef3 0%,#b8c2cc 45%,#6d6a5f 100%);border-radius:14px}
.card{width:345px;height:250px;background:var(--card);border-radius:3px;color:var(--white);text-align:center}
.card h3{position:absolute;left:0;right:0;top:66px;font-size:18px;font-weight:700}
.card p{position:absolute;left:22px;right:22px;top:111px;font-size:13px;line-height:19.7px;color:#eee}
.badge{width:94px;height:94px;border-radius:50%;top:-47px;left:50%;margin-left:-47px}
.footer{left:0;top:1991px;width:1200px;height:415px;background:var(--footer);color:var(--white)}
.footer h4{position:absolute;top:52px;font-size:18px;font-weight:700;color:#fff}
.f-text{font-size:13.5px;line-height:19.5px;color:#f2f7ff}
.social{display:flex;gap:14px}
.social span{width:11px;height:11px;border-radius:50%;background:#fff;display:block}
.post{left:332px;width:260px;height:48px}
.post-thumb{left:0;top:0;width:48px;height:48px;border-radius:50%;background:#c5c8cc;color:#555;font-size:10px;display:flex;align-items:center;justify-content:center}
.post-title{left:63px;top:4px;font-size:13.5px;color:#fff}
.post-meta{left:63px;top:26px;font-size:11.5px;color:#f2f7ff}
.quote-mark{left:895px;top:88px;font-size:64px;font-weight:700;color:#3a76c9;line-height:64px}
.avatar{left:895px;top:2208px;width:78px;height:78px;border-radius:50%;background:#c8cacd;color:#333;font-size:13px;display:flex;align-items:center;justify-content:center}
.footer-rule{left:53px;top:349px;width:1094px;border-top:1.5px solid var(--footer-line)}
.copyright{left:0;top:377px;width:1200px;text-align:center;font-size:13px;color:#f2f7ff}
</style>
</head>
<body>

<header class="abs topbar"><span class="brand">Bright Years Forward</span></header>

<section class="abs hero" role="img" aria-label="Photo of a runner's legs on a mountain trail under a cloudy sky"></section>
<nav class="abs nav">
  <a style="left:185px">Apex care</a>
  <a style="left:327px">Apex slim</a>
  <a style="left:464px">Apex motion</a>
  <a style="left:569px">Apx plate</a>
  <a style="left:683px">ApexDailyMix</a>
  <a style="left:836px">Apex academy</a>
  <a class="login" style="left:961px">Login</a>
</nav>
<h1 class="abs hero-title">Ready to Enjoy?</h1>
<p class="abs hero-sub">Grab This Perfect Team Now!</p>
<a class="abs btn btn-buy">I like it! Purchase</a>
<a class="abs btn btn-surf">Go on surfing</a>

<h2 class="abs section-title" style="top:594px">Health And Wellness</h2>
<div class="abs rule" style="top:634px"></div>

<div class="abs mission-label">OUR MISSION AND VISION:</div>
<p class="abs mission-text">To provide clients cutting edge anti aging programs and protocols designed to "turn-back-the-clock-one-second-at-a-time.<br>Let's all Bright Years Forward..together!</p>

<div class="abs devices" role="img" aria-label="Website shown on laptop, tablet and phone screens"></div>

<h2 class="abs section-title" style="top:1234px">Bright Years Forward's Program Consists</h2>
<div class="abs rule" style="top:1275px"></div>

<article class="abs card" style="left:53px;top:1344px">
  <div class="abs badge" style="background:var(--care)" role="img" aria-label="Figure in a yoga pose"></div>
  <h3>Apex care</h3>
  <p>A medical doctor supervised unique and proprietary hormone optimization program and protocol developed by a board certified medical doctor trained by Volarix ( a world leader in age management medicine) who has practiced age management medicine for the past 7 years</p>
</article>
<article class="abs card" style="left:427px;top:1344px">
  <div class="abs badge" style="background:var(--slim)" role="img" aria-label="Figure stretching"></div>
  <h3>Apex slim</h3>
  <p>A medical doctor supervised unique and proprietary weight management program and protocol developed by a published medical doctor who's diet book "Fresh start: Shed those pounds soon" was just launched</p>
</article>
<article class="abs card" style="left:800px;top:1344px">
  <div class="abs badge" style="background:var(--motion)" role="img" aria-label="Figure exercising"></div>
  <h3>Apex motion</h3>
  <p>A master athlete supervised training program and protocol, with access to a large proprietary exercise video databank developed by a 7th degree black belt jiu-jitsu master</p>
</article>

<article class="abs card" style="left:53px;top:1713px">
  <div class="abs badge" style="background:var(--plate)" role="img" aria-label="Figure with raised arms"></div>
  <h3>Apx plate</h3>
  <p>A chef driven and supervised home delivered healthy meals. Each meal is made from scratch, and is specifically tailored and targeted according to each patient's specific needs</p>
</article>
<article class="abs card" style="left:423px;top:1713px">
  <div class="abs badge" style="background:var(--mix)" role="img" aria-label="Figure in a floor stretch"></div>
  <h3>ApexDailyMix</h3>
  <p>A doctor formulated-master athlete approved most complete multi vitamin-mineral-anti-oxidant and supplement pack available on the market today. ApexDailyMix is: made in the USA, and QSA approved vitamin factory, gluten free, sugar free, and artificial color free.</p>
</article>
<article class="abs card" style="left:794px;top:1713px">
  <div class="abs badge" style="background:var(--academy)" role="img" aria-label="Seated figure"></div>
  <h3>Apex academy</h3>
  <p>A unique CME approved teaching workshop intended for those physicians who lack expertise in age management but want to become proficient in the art of hormone optimization and age management medicine. The 2-day workshop is held twice monthly on Saturday and Sunday in sunny Florida</p>
</article>

<footer class="abs footer">
  <h4 style="left:53px">Contact Us</h4>
  <p class="abs f-text" style="left:53px;top:92px;width:245px">Maecenas etos sit amet, consectetur adipiscing elit. Terminal volutpat rutrum metro amet sollicitudin interdum.</p>
  <p class="abs f-text" style="left:53px;top:166px">Phone: +1 (800) 555 01 23</p>
  <p class="abs f-text" style="left:53px;top:200px">Office: 2140 Elm Avenue, Portland</p>
  <p class="abs f-text" style="left:53px;top:234px">Email: hello@brightyears.example</p>
  <div class="abs social" style="left:53px;top:276px"><span></span><span></span><span></span><span></span><span></span></div>

  <h4 style="left:334px">Recent Posts</h4>
  <h4 style="left:614px">Latest Twitts</h4>
  <h4 style="left:895px">Last Review</h4>

  <div class="abs quote-mark">&ldquo;</div>
  <p class="abs f-text" style="left:951px;top:92px;width:200px">Lorem ipsum dolor sit amet, consectetur adipiscing elit, sed do eiusmod tempor incididunt ut labore et dolore magna aliqua. Ut enim ad minim veniam, quis nostrud exercitation ullamco.</p>
  <p class="abs" style="left:990px;top:231px;font-size:16px;color:#fff">Dana Whitfield</p>
  <p class="abs" style="left:990px;top:262px;font-size:12.5px;color:#fff">Creative Designer</p>

  <div class="abs footer-rule"></div>
  <p class="abs copyright">Copyright 2020. All Rights Reserved by Bright Years Forward's</p>
</footer>

<div class="abs post" style="top:2087px">
  <div class="abs post-thumb">50x50</div>
  <div class="abs post-title">Business Cards Design Trends</div>
  <div class="abs post-meta">Dec 02, 2020 / 2 comments</div>
</div>
<div class="abs post" style="top:2159px">
  <div class="abs post-thumb">50x50</div>
  <div class="abs post-title">This Maravelous App</div>
  <div class="abs post-meta">Nov 18, 2020 / 9 comments</div>
</div>
<div class="abs post" style="top:2231px">
  <div class="abs post-thumb">50x50</div>
  <div class="abs post-title">Brand Paper Niceties</div>
  <div class="abs post-meta">Nov 10, 2020 / 0 comments</div>
</div>
<div class="abs avatar">84x84</div>

</body>
</html>
```